Building company buisness cards

We are looking for a sharp modern new look for our business cards.We are a New Zealand based company that specialises in house and land packages.We have attached a photo of the current logo and would like to see if it can be improved somehow if needed.We are open to any colours but we have chosen Black and White at this stage. Feel free to change the font and make the logo smarter looking.Play with the colours and see what looks best.We want a card that looks so good know one will want to throw it away!

Target Market(s)

Building profesonals, home buyers

Industry/Entity Type

Building

Contact Information for Business Card

Derek Haskins
0274930268
derekh@stonerange.co.nz

Font styles to use
Serif
Sans Serif

Colors

Designer to choose colors to be used in the design.

Requirements
Must have
• Just the logo on one side and details on the other
• Clean simple looking card
Nice to have
• Round corners and detail like raised or spot UV
• Something that stands out
Should not have
• To title needed, Director etc

```html
<!DOCTYPE html>
<html lang="en">
<head>
<meta charset="utf-8">
<title>Stonerange business card – front and back</title>
<link rel="stylesheet" href="https://fonts.googleapis.com/css2?family=Jost:wght@400;500&display=swap">
<style>
  :root {
    --backdrop: #1d1e20;
    --card: #3b3c3e;
    --card-edge: #333436;
    --brand-tone: #4a4b4e;
    --ink: #f4f4f2;
    --ink-soft: #d9d9d6;
    --label: #ffffff;
  }
  * { margin: 0; padding: 0; box-sizing: border-box; }
  html, body {
    width: 1200px;
    height: 591px;
    overflow: hidden;
    background: var(--backdrop);
    font-family: "Jost", "Futura", sans-serif;
  }
  .sheet {
    position: relative;
    width: 1200px;
    height: 591px;
    display: flex;
    justify-content: center;
    align-items: center;
    gap: 60px;
  }
  .side {
    position: relative;
  }
  .side-label {
    position: absolute;
    top: -44px;
    left: 0;
    color: var(--label);
    font-size: 20px;
    font-weight: 500;
  }
  .card {
    position: relative;
    width: 520px;
    height: 289px;
    background: var(--card);
    border: 1px solid var(--card-edge);
    border-radius: 14px;
    overflow: hidden;
  }
  .brand-name {
    color: var(--brand-tone);
    font-weight: 500;
    white-space: nowrap;
  }

  /* Front: contact details */
  .contact {
    position: absolute;
    left: 52px;
    top: 150px;
  }
  .contact-name {
    color: var(--ink);
    font-size: 27px;
    font-weight: 400;
    letter-spacing: 0.5px;
    margin-bottom: 12px;
  }
  .contact-line {
    color: var(--ink-soft);
    font-size: 14px;
    letter-spacing: 0.6px;
    line-height: 24px;
  }
  .front-brand {
    position: absolute;
    right: 44px;
    top: 120px;
    font-size: 26px;
    letter-spacing: 1px;
  }

  /* Back: brand only */
  .brand-lockup {
    position: absolute;
    inset: 0;
    display: flex;
    align-items: center;
    justify-content: center;
  }
  .brand-lockup .brand-name {
    font-size: 52px;
    letter-spacing: 0.5px;
  }
</style>
</head>
<body>
  <main class="sheet">
    <section class="side side-front">
      <p class="side-label">front</p>
      <div class="card card-front">
        <div class="contact">
          <p class="contact-name">Derek Haskins</p>
          <p class="contact-line">0274930268</p>
          <p class="contact-line">derekh@stonerange.co.nz</p>
        </div>
        <p class="brand-name front-brand">Stonerange</p>
      </div>
    </section>

    <section class="side side-back">
      <p class="side-label">back</p>
      <div class="card card-back">
        <div class="brand-lockup">
          <p class="brand-name">Stonerange</p>
        </div>
      </div>
    </section>
  </main>
</body>
</html>
```